Business Card Design For Marketing Agnecy LWP

Need business card design for marketing agency.

Dorian Pellow
President, CEO
1-555-302-4196
dorian@brightlanepromotions.example
www.BrightlanePromotions.example

Back Side:
Boost Sales Using Rewards, Incentives & Giveaways
Get A Free Sample Package

Target Market(s)

B2B

Industry/Entity Type

Marketing

Contact Information for Business Card

Dorian Pellow
President, CEO
1-555-302-4196

Back Side:
Get A Free Sample Package

Please note that my current url is OLD DESIGN. I am working on new design and want the business card to match color themes at least on new site. Here is the demo link for new site so you can see the colors I use, etc.

http://pixelquarrydemo.example/dh/dorian/lwp_final/index.html

Requirements
Must have
• Please note that my current url is OLD DESIGN. I am working on new design and want the business card to match color themes at least on new site. Here is the demo link for new site so you can see the colors I use, etc.

Nice to have

Should not have

```html
<!DOCTYPE html>
<html lang="en">
<head>
<meta charset="utf-8">
<title>LWP Business Card</title>
<link href="https://fonts.googleapis.com/css2?family=Lato:ital,wght@0,400;0,700;0,900;1,400;1,700&display=swap" rel="stylesheet">
<style>
  :root {
    --brand-blue: #1076be;
    --ink-grey: #4f4f52;
    --paper: #ffffff;
    --backdrop: #2a2a2a;
  }
  * { margin: 0; padding: 0; box-sizing: border-box; }
  html, body { width: 1200px; height: 1200px; overflow: hidden; }
  body {
    position: relative;
    background: var(--backdrop);
    font-family: "Lato", Arial, sans-serif;
  }
  .card {
    position: absolute;
    left: 235px;
    width: 730px;
    height: 417px;
  }
  .card-front { top: 160px; background: var(--brand-blue); color: var(--paper); text-align: center; }
  .card-back { top: 625px; background: var(--paper); color: var(--ink-grey); }

  .brand-lockup { position: absolute; font-weight: 900; }
  .brand-mark { line-height: 0.9; letter-spacing: 2px; }
  .brand-name { letter-spacing: 3px; line-height: 1.1; }

  .card-front .brand-lockup { left: 0; right: 0; top: 72px; display: flex; flex-direction: column; align-items: center; }
  .card-front .brand-mark { font-size: 130px; }
  .card-front .brand-name { font-size: 22px; margin-top: 16px; }

  .tagline { position: absolute; left: 0; right: 0; top: 302px; font-size: 17px; }
  .offer { position: absolute; left: 0; right: 0; top: 333px; font-size: 17px; font-weight: 700; }
  .front-url { position: absolute; left: 0; right: 0; top: 356px; font-size: 20px; font-style: italic; }
  .front-url strong { font-weight: 700; }

  .card-back .brand-lockup { left: 45px; top: 44px; color: var(--brand-blue); }
  .card-back .brand-mark { font-size: 104px; }
  .card-back .brand-name { font-size: 18px; margin-top: 12px; }

  .person { position: absolute; left: 45px; top: 226px; }
  .person-name { font-size: 29px; font-weight: 900; color: var(--brand-blue); letter-spacing: 0.5px; line-height: 1.1; }
  .person-title { font-size: 18px; line-height: 1.2; }

  .contact-list { position: absolute; left: 42px; top: 306px; list-style: none; font-size: 17px; }
  .contact-list li { display: flex; align-items: center; gap: 10px; height: 24px; }
  .contact-list svg { width: 18px; height: 18px; fill: var(--brand-blue); flex: none; }

  .address {
    position: absolute; left: 456px; top: 330px;
    border-left: 3px solid var(--ink-grey);
    padding-left: 13px; font-size: 17px; line-height: 24px; font-style: normal;
  }
</style>
</head>
<body>

<section class="card card-front">
  <div class="brand-lockup">
    <div class="brand-mark">LWP</div>
    <div class="brand-name">BRIGHTLANE PROMOTIONS</div>
  </div>
  <p class="tagline">Boost Sales Using Rewards, Incentives &amp; Giveaways</p>
  <p class="offer">Get A Free Sample Package</p>
  <p class="front-url">www.<strong>BrightlanePromotions</strong>.example</p>
</section>

<section class="card card-back">
  <div class="brand-lockup">
    <div class="brand-mark">LWP</div>
    <div class="brand-name">BRIGHTLANE PROMOTIONS</div>
  </div>

  <div class="person">
    <h1 class="person-name">DORIAN PELLOW</h1>
    <p class="person-title">President, CEO</p>
  </div>

  <ul class="contact-list">
    <li>
      <svg viewBox="0 0 24 24" aria-hidden="true"><path d="M6.6 10.8a15.1 15.1 0 0 0 6.6 6.6l2.2-2.2c.3-.3.7-.4 1-.2 1.1.4 2.3.6 3.6.6.6 0 1 .4 1 1V20c0 .6-.4 1-1 1A17 17 0 0 1 3 4c0-.6.4-1 1-1h3.5c.6 0 1 .4 1 1 0 1.3.2 2.5.6 3.6.1.3 0 .7-.2 1z"/></svg>
      <span>1-555-302-4196</span>
    </li>
    <li>
      <svg viewBox="0 0 24 24" aria-hidden="true"><path d="M2 5h20v2l-10 6L2 7z M2 9l10 6 10-6v10H2z"/></svg>
      <span>dorian@brightlanepromotions.example</span>
    </li>
    <li>
      <svg viewBox="0 0 24 24" aria-hidden="true"><path d="M12 2a10 10 0 1 0 0 20 10 10 0 0 0 0-20zm0 2c.9 1.2 1.6 2.6 2 4h-4c.4-1.4 1.1-2.8 2-4zM4.3 14a8 8 0 0 1 0-4h3.5a16 16 0 0 0 0 4zm.9 2h3c.3 1.3.8 2.5 1.5 3.6A8 8 0 0 1 5.2 16zm3-8h-3a8 8 0 0 1 4.5-3.6C8.9 5.5 8.5 6.7 8.2 8zM12 20c-.9-1.2-1.6-2.6-2-4h4c-.4 1.4-1.1 2.8-2 4zm2.3-6H9.7a14 14 0 0 1 0-4h4.6a14 14 0 0 1 0 4zm.2 5.6c.7-1.1 1.2-2.3 1.5-3.6h3a8 8 0 0 1-4.5 3.6zM16.2 14a16 16 0 0 0 0-4h3.5a8 8 0 0 1 0 4zm-.2-6c-.3-1.3-.8-2.5-1.5-3.6A8 8 0 0 1 18.8 8z"/></svg>
      <span>www.BrightlanePromotions.example</span>
    </li>
  </ul>

  <address class="address">
    418 Harbor Ridge Way<br>
    Fairview, CA 90210, USA
  </address>
</section>

</body>
</html>
```